Thai Menu Design Project

We need a new menu design for a Thai restaurant in Fort Worth, Texas. We are a family-owned and really proud about our food and our service. We want the menu to feel healthy, modern, delicious, artistic Thai, and friendly. The colors we used in our restaurant are maroon, burgundy, black, white, gold and pale yellow.

Please look at our website www.brindlewokery.com
for the reference of the menus and the photos we use.

The menu can be in any number of pages (the fewer the better though) The size of the paper is US letter.
Updates

Update:

- We don't put the photos of the food in the menu pages anymore, instead, we like to put the photos of the herbs and their benefits (found in the file 'herb benefits') on the menu pages instead.

- the paper size is US letter.

- we don't have specific numbers of pages but the fewer the better

Thank you!

I added logos and background photo again in case the previous files did not work. Thanks!

Target Market(s)

Trendy socialized people from 20-30s,couples of all ages from 20s-60s,and families.

Industry/Entity Type

Restaurant

Requirements
Must have
• We want the menu to feel healthy, modern, delicious, artistic, Thai, and friendly.

We like to keep the colors maroon, burgundy, black, gold, pale yellow, and off white.

We like to put the photos of the herbs and their benefits (available in the file called 'herb benefits') randomly in the menu pages.

*Please use the photos available in the file called 'herb benefits' along with its details somewhere in the pages. You can change the photo of each herb to the ones you find more fitting from the internet.

Nice to have
• If we can add the wallpaper pattern in our menu it will be great. It can be used in anyway.

```html
<!DOCTYPE html>
<html lang="en">
<head>
<meta charset="utf-8">
<title>Brindle Wokery – Menu Pages 4 and 5</title>
<link href="https://fonts.googleapis.com/css2?family=Lora:ital,wght@1,600;1,700&family=Open+Sans:ital,wght@0,400;0,600;1,300&display=swap" rel="stylesheet">
<style>
  :root{
    --backdrop-light:#f4f4f4;
    --backdrop-dark:#cfcfd1;
    --frame-maroon:#4f1427;
    --frame-gold:#a8833f;
    --gold-line:#b8975a;
    --paper:#f4efec;
    --paper-tint:#e9e0e6;
    --maroon:#7b1020;
    --plum:#6e1a63;
    --ink:#2b2326;
    --ink-soft:#3d3235;
    --chili:#b3141f;
    --badge:#c9a24b;
    --herb-box:#7a1326;
    --white:#ffffff;
  }
  *{box-sizing:border-box;margin:0;padding:0}
  html,body{width:1200px;height:800px;overflow:hidden}
  body{
    position:relative;
    background:radial-gradient(ellipse at 50% 45%,var(--backdrop-light) 0%,var(--backdrop-dark) 100%);
    font-family:"Open Sans",Arial,sans-serif;
    color:var(--ink);
  }
  .page-label{
    position:absolute;top:38px;width:518px;text-align:center;
    font-style:italic;font-weight:300;font-size:27px;color:var(--white);letter-spacing:.5px;
  }
  .page{position:absolute;top:93px;width:518px;height:671px}
  .page--four{left:37px}
  .page--five{left:646px}
  .page-label--four{left:37px}
  .page-label--five{left:646px}

  .page__border{
    position:absolute;inset:0;
    background:
      radial-gradient(circle at 30% 20%,rgba(168,131,63,.55) 0 8%,transparent 30%),
      radial-gradient(circle at 70% 80%,rgba(168,131,63,.5) 0 8%,transparent 30%),
      linear-gradient(135deg,var(--frame-maroon) 0%,#6b4a2c 50%,var(--frame-maroon) 100%);
    box-shadow:0 2px 6px rgba(0,0,0,.25);
  }
  .page__paper{
    position:absolute;left:22px;top:24px;right:22px;bottom:23px;overflow:hidden;
    background:radial-gradient(ellipse at 50% 40%,var(--paper) 0%,var(--paper) 55%,var(--paper-tint) 100%);
    border:1px solid var(--gold-line);
  }
  .page__paper::before{
    content:"";position:absolute;inset:5px;border:1px solid var(--gold-line);pointer-events:none;
  }
  .page__pattern{position:absolute;inset:6px;
    background:radial-gradient(ellipse at 50% 50%,rgba(226,214,222,.55),rgba(226,214,222,0) 70%);}

  .brand{
    position:absolute;top:28px;left:0;right:0;
    display:flex;align-items:center;justify-content:center;gap:8px;
    font-weight:600;font-size:17px;color:var(--plum);
  }
  .brand__dot{width:12px;height:12px;border-radius:50%;background:var(--plum)}

  .section-title{
    font-family:"Lora",Georgia,serif;font-style:italic;font-weight:700;
    font-size:29px;line-height:1;color:var(--maroon);
  }
  .section-title--plum{color:var(--plum)}
  .section-sub{font-size:11px;line-height:13px;color:var(--maroon)}
  .col{position:absolute}
  .item{margin-bottom:7px}
  .line{display:flex;align-items:baseline;font-size:11px;line-height:13px;color:var(--ink)}
  .name{white-space:nowrap}
  .dots{flex:1;border-bottom:1.6px dotted var(--ink-soft);margin:0 2px 2px;min-width:8px}
  .price{white-space:nowrap}
  .desc{font-size:8px;line-height:10.5px;color:var(--ink-soft);margin-top:2px}
  .note{font-size:8px;line-height:11px;color:var(--maroon);white-space:nowrap}
  .chili{
    display:inline-block;width:3px;height:9px;margin-left:4px;
    background:var(--chili);border-radius:2px 2px 3px 3px;transform:rotate(18deg);
  }
  .badge{
    display:inline-block;margin-left:4px;padding:0 4px;height:10px;line-height:10px;
    border-radius:5px;background:var(--badge);color:var(--white);
    font-size:6px;font-weight:600;vertical-align:2px;
  }
  .divider{position:absolute;left:238px;top:90px;width:1px;height:430px;background:var(--gold-line)}

  .policy{
    position:absolute;left:254px;top:548px;width:200px;height:56px;
    background:var(--white);border:1px solid var(--maroon);border-radius:4px;
    font-size:8px;line-height:10.5px;text-align:center;color:var(--maroon);padding:6px 8px;
  }

  .herb{
    position:absolute;left:252px;top:446px;width:198px;height:168px;
    background:var(--herb-box);color:var(--white);padding:6px 8px;
  }
  .herb__title{position:relative;font-weight:600;font-size:13px;letter-spacing:.5px;margin-bottom:2px}
  .herb__text{position:relative;font-size:6.3px;line-height:8.7px}
  .herb__photo{
    position:absolute;right:-6px;top:4px;width:92px;height:62px;border-radius:45% 50% 40% 55%;
    background:radial-gradient(ellipse at 45% 45%,#8fbf4a 0%,#5f9a2f 55%,rgba(95,154,47,0) 75%);
  }
</style>
</head>
<body>

<div class="page-label page-label--four">Page 4</div>
<div class="page-label page-label--five">Page 5</div>

<section class="page page--four">
  <div class="page__border" role="img" aria-label="Gold damask wallpaper pattern on a maroon border"></div>
  <div class="page__paper">
    <div class="page__pattern" role="img" aria-label="Faint damask pattern on the paper"></div>
    <div class="brand"><span class="brand__dot"></span>Brindle Wokery</div>

    <div class="col" style="left:22px;top:88px;width:186px">
      <h2 class="section-title">Curries</h2>
      <p class="section-sub" style="margin-top:2px">Choice of Chicken, Beef, Pork,<br>Tofu or Mixed Vegetable</p>
      <div style="margin-top:12px">
        <div class="line" style="margin-bottom:1px"><span class="name">Meat Combo (2)</span><span class="dots"></span><span class="price">add 2</span></div>
        <div class="line" style="margin-bottom:1px"><span class="name">Shrimp or Fish Balls (4)</span><span class="dots"></span><span class="price">add 2.50</span></div>
        <div class="line"><span class="name">Seafood Combo</span><span class="dots"></span><span class="price">add 4</span></div>
        <p class="note" style="margin:2px 0 17px">All dishes served with Jasmine rice or brown rice.</p>
      </div>

      <div class="item"><div class="line"><span class="name">Red Curry<i class="chili"></i></span><span class="dots"></span><span class="price">12</span></div>
        <p class="desc">Red chili, herbs, shrimp paste, bamboo shoots, basil, and bell pepper in coconut milk</p></div>
      <div class="item"><div class="line"><span class="name">Massaman Curry<i class="chili"></i></span><span class="dots"></span><span class="price">12</span></div>
        <p class="desc">Southern Thai spices blended in chili paste with potatoes, onion and cashew nuts, simmered in coconut milk</p></div>
      <div class="item"><div class="line"><span class="name">Green Curry<i class="chili"></i></span><span class="dots"></span><span class="price">12</span></div>
        <p class="desc">Curry with green chili aroma, bamboo shoots, eggplant, basil, and bell pepper in coconut milk</p></div>
      <div class="item"><div class="line"><span class="name">Panang Curry<i class="chili"></i></span><span class="dots"></span><span class="price">12</span></div>
        <p class="desc">Curry with strong flavor of cumin and coriander seed, hint of kaffir lime leaves, and bell pepper simmered in coconut milk</p></div>
      <div class="item"><div class="line"><span class="name">Jungle Curry<i class="chili"></i></span><span class="dots"></span><span class="price">12</span></div>
        <p class="desc">Eastern style hot chili paste stir-fried with green beans, bell peppers, and bamboo shoots<br>(no coconut milk)</p></div>
      <div class="item"><div class="line"><span class="name">Yellow Curry<i class="chili"></i></span><span class="dots"></span><span class="price">12</span></div>
        <p class="desc">Curry with aroma of cardamom, cinnamon and turmeric in coconut milk with peas and carrots simmered in coconut milk</p></div>
      <div class="item"><div class="line"><span class="name">Gaeng Kua Pineapple<i class="chili"></i></span><span class="dots"></span><span class="price">12</span></div>
        <p class="desc">Gaeng Kua curry paste with pineapple chunks simmered in coconut milk</p></div>
    </div>

    <div class="divider"></div>

    <div class="col" style="left:254px;top:88px;width:200px">
      <h2 class="section-title section-title--plum">Vegetarian</h2>
      <div style="margin-top:16px">
        <div class="item"><div class="line"><span class="name">Vegetarian Larb<i class="chili"></i><span class="badge">NEW</span></span><span class="dots"></span><span class="price">11.5</span></div>
          <p class="desc">North-Eastern spicy salad seasoned with herbs, shallots, scallions, roasted ground rice in spicy lime juice</p>
          <p class="desc" style="margin-top:4px">Choice of Vegetarian Duck, Vegetarian Chicken or Soft Tofu</p></div>
        <div class="item" style="margin-top:12px"><div class="line"><span class="name">Vegetarian Chicken or Duck</span></div>
          <div class="line"><span class="name">Lettuce Wrap (V)</span><span class="dots"></span><span class="price">11.5</span></div>
          <p class="desc">Minced vegetarian meat with water chestnuts, mushrooms, scallions, crispy noodles and cool lettuce cups with spicy lime sauce</p></div>
        <p class="note" style="color:var(--plum);margin:10px 0 10px">All dishes below served with Jasmine or brown rice</p>
        <div class="item"><div class="line"><span class="name">Pad Kra Prow Eggplant, Tofu or</span></div>
          <div class="line"><span class="name">Vegetarian Duck<i class="chili"></i></span><span class="dots"></span><span class="price">11.5</span></div>
          <p class="desc">Stir-fried with fresh basil, jalapenos, garlic, baby corn, and bell peppers</p></div>
        <div class="item"><div class="line"><span class="name">Chili Mushroom<i class="chili"></i></span><span class="dots"></span><span class="price">11.5</span></div>
          <p class="desc">3 kinds of mushrooms sautéed with fresh chili and fresh garlic</p></div>
        <div class="item"><div class="line"><span class="name">Kee Mao Hed<i class="chili"></i></span><span class="dots"></span><span class="price">11.5</span></div>
          <p class="desc">Stir-fried mixed mushrooms with sweet basil, chili, bell pepper, onion</p></div>
        <div class="item"><div class="line"><span class="name">Mixed Vegetables</span><span class="dots"></span><span class="price">11.5</span></div>
          <p class="desc">Stir-fried mixed vegetables in bean sauce</p></div>
        <div class="item"><div class="line"><span class="name">Vegetable Curry</span><span class="dots"></span><span class="price">11.5</span></div>
          <p class="desc">Mixed vegetables, bamboo shoots, soft tofu, basil and bell pepper with red curry paste in coconut milk</p></div>
      </div>
    </div>

    <div class="policy">
      <i class="chili" style="margin:0 3px 0 0"></i>For spicy dishes, please choose spicy level from 1 to 5.<br>(V) for Vegetarian.<br>Up to 5 credit cards per check please.
    </div>
  </div>
</section>

<section class="page page--five">
  <div class="page__border" role="img" aria-label="Gold damask wallpaper pattern on a maroon border"></div>
  <div class="page__paper">
    <div class="page__pattern" role="img" aria-label="Faint damask pattern on the paper"></div>
    <div class="brand"><span class="brand__dot"></span>Brindle Wokery</div>

    <div style="position:absolute;left:20px;top:88px;display:flex;align-items:baseline;gap:9px">
      <h2 class="section-title">Entrees</h2>
      <p class="section-sub">Choice of Chicken, Beef, Pork, Tofu, or Mixed Vegetables</p>
    </div>

    <div class="col" style="left:20px;top:134px;width:200px">
      <div class="item"><div class="line"><span class="name">Pad Kra Prow<i class="chili"></i></span><span class="dots"></span><span class="price">11.5</span></div>
        <p class="desc">Sautéed fresh basil, chili, garlic, jalapenos and bell pepper</p></div>
      <div class="item"><div class="line"><span class="name">Cashew Nuts</span><span class="dots"></span><span class="price">11.5</span></div>
        <p class="desc">Roasted cashew nuts with onion, scallions, red bell pepper, carrot, baby corn with chili paste</p></div>
      <div class="item"><div class="line"><span class="name">Lemon Chicken / Shrimp<span class="badge">NEW</span></span><span class="dots"></span><span class="price">11.5</span></div>
        <p class="desc">Crispy chicken or shrimp with sweet and sour lemon sauce. For shrimp adds 2.5</p></div>
      <div class="item"><div class="line"><span class="name">Pad Ginger</span><span class="dots"></span><span class="price">11.5</span></div>
        <p class="desc">Fresh ginger, onion, scallions, red bell pepper, and mushrooms</p></div>
      <div class="item"><div class="line"><span class="name">Wild Bangkok<i class="chili"></i></span><span class="dots"></span><span class="price">11.5</span></div>
        <p class="desc">Sautéed bamboo shoots, baby corn, ginger key, bell pepper and fresh basil in spicy chili sauce</p></div>
      <div class="item"><div class="line"><span class="name">Black Pepper Beef<i class="chili"></i></span><span class="dots"></span><span class="price">11.5</span></div>
        <p class="desc">Beef, scallions, red pepper, onion and peppercorns in black pepper sauce served on a hot plate</p></div>
      <div class="item"><div class="line"><span class="name">Pad Prik Khing<i class="chili"></i></span><span class="dots"></span><span class="price">11.5</span></div>
        <p class="desc">Sir-fried with green beans, bell pepper, and dried chili paste</p></div>
      <div class="item"><div class="line"><span class="name">House Chili<span class="badge">NEW</span></span><span class="dots"></span><span class="price">11.5</span></div>
        <p class="desc">Thai-style sweet chili paste sautéed with bell pepper, baby corn, onion and carrot</p></div>
      <div class="item"><div class="line"><span class="name">Basil Sauce<i class="chili"></i></span><span class="dots"></span><span class="price">11.5</span></div>
        <p class="desc">Sautéed with bamboo shoots, garlic, bell pepper, jalapenos and basil</p></div>
      <div class="item"><div class="line"><span class="name">Garlic Sauce</span><span class="dots"></span><span class="price">11.5</span></div>
        <p class="desc">Sautéed garlic, steamed broccoli, carrot in garlic sauce</p></div>
      <div class="item"><div class="line"><span class="name">Hot Pepper<i class="chili"></i></span><span class="dots"></span><span class="price">11.5</span></div>
        <p class="desc">Stir-fried onion, jalapenos, bell pepper, basil leaves in house pepper sauce</p></div>
    </div>

    <div class="col" style="left:252px;top:134px;width:198px">
      <div class="item"><div class="line"><span class="name">Orange Chicken</span><span class="dots"></span><span class="price">11.5</span></div>
        <p class="desc">Boneless chicken breast and broccoli in Oriental style orange sauce</p></div>
      <div class="item"><div class="line"><span class="name">Lemongrass</span><span class="dots"></span><span class="price">11.5</span></div>
        <p class="desc">Stir-fried bell pepper, onion, and carrot in house lemongrass sauce</p></div>
      <div class="item"><div class="line"><span class="name">Peanut Sauce</span><span class="dots"></span><span class="price">11.5</span></div>
        <p class="desc">Choice of meat, tofu, or mixed vegetables in peanut sauce served on a bed of steamed broccoli</p></div>
      <div class="item"><div class="line"><span class="name">Bangkok BBQ Pork</span><span class="dots"></span><span class="price">11.5</span></div>
        <p class="desc">Marinated grilled pork with special sauce</p></div>
      <div class="item"><div class="line"><span class="name">Teriyaki Chicken or Beef</span><span class="dots"></span><span class="price">11.5</span></div>
        <p class="desc">Marinated grilled chicken breast or beef topped with teriyaki sauce and sesame seeds</p></div>
      <div style="margin-top:12px">
        <div class="line" style="margin-bottom:1px"><span class="name">Meat Combo (2)</span><span class="dots"></span><span class="price">add 2</span></div>
        <div class="line" style="margin-bottom:1px"><span class="name">Shrimp</span><span class="dots"></span><span class="price">add 2.5</span></div>
        <div class="line"><span class="name">Seafood Combo</span><span class="dots"></span><span class="price">add 4</span></div>
        <p class="note" style="margin:2px 0 3px">All dishes served with Jasmine rice or brown rice.</p>
        <div class="line" style="margin-bottom:2px"><span class="name">For Sticky rice</span><span class="dots"></span><span class="price">add 2.5</span></div>
        <div class="line" style="font-size:10px"><span class="name">Thai it up with Kai Dao (crispy fried egg)</span><span class="dots"></span><span class="price">2</span></div>
      </div>
    </div>

    <div class="herb">
      <div class="herb__photo" role="img" aria-label="Photo of fresh basil leaves"></div>
      <h3 class="herb__title">BASIL</h3>
      <p class="herb__text">The king of herbs, basil is one of the<br>oldest and popular herbal plants.<br>This highly prized plant is revered<br>as "holy herb" in many traditions<br>all around the world. The name "basil" comes from the ancient Greek word basilikohn, meaning "royal". Basil is originally native to Iran, India and other tropical regions of Asia, and is grown for its medicinally useful leaves and seeds Its oils and extracts are said to have antioxidant and antibacterial properties. Other benefits of basil include cancer prevention, skin and hair health, bone and connective tissue, digestive tract health, anti-bacterial, immune system.</p>
    </div>
  </div>
</section>

</body>
</html>
```